Criação de Kit Layout de Posts para Redes Sociais (Facebook, Instagram e etc) para Esportes
" Ofereço serviços de personal trainer para alunos em academias, condomínios, parques, etc.; serviços de personal trainer on-line ao vivo; e serviços de consultoria para prescrição de treinos (sem o acompanhamento durante a execução em si dos treinos) "

```html
<!DOCTYPE html>
<html lang="pt-BR">
<head>
<meta charset="UTF-8">
<title>Personal Trainer – Post</title>
<link rel="stylesheet" href="https://fonts.googleapis.com/css2?family=Archivo+Black&family=Montserrat:ital,wght@0,700;0,800;0,900;1,800;1,900&display=swap">
<style>
  :root {
    --green: #3fe04a;
    --green-dark: #1f9a28;
    --ink: #0d0f0d;
    --panel: #141614;
    --white: #ffffff;
    --grey: #2c2f2c;
  }
  * { margin: 0; padding: 0; box-sizing: border-box; }
  html, body { width: 1200px; height: 1200px; overflow: hidden; background: var(--ink); }
  .post {
    position: relative; width: 1200px; height: 1200px; overflow: hidden;
    font-family: "Montserrat", sans-serif; color: var(--white);
  }
  .gym-photo {
    position: absolute; inset: 0;
    background:
      radial-gradient(ellipse 420px 620px at 830px 560px, #b48a6c 0%, #7a5a45 30%, rgba(40,38,36,0) 75%),
      linear-gradient(180deg, #3a3c3a 0%, #232523 45%, #4a4a46 75%, #6a6a64 100%);
  }
  .shade {
    position: absolute; inset: 0;
    background: linear-gradient(90deg, rgba(10,12,10,.85) 0%, rgba(10,12,10,.55) 45%, rgba(10,12,10,0) 70%);
  }
  .accents { position: absolute; inset: 0; }
  .brand {
    position: absolute; left: 24px; top: 48px; width: 564px; height: 228px;
    display: flex; flex-direction: column; align-items: center; justify-content: center;
    padding-right: 60px;
    background: rgba(13,15,13,.92);
  }
  .brand-frame { position: absolute; inset: 0; }
  .brand-mark { position: relative; width: 42px; height: 42px; background: var(--green); margin-bottom: 18px; }
  .brand-name {
    position: relative; font-family: "Montserrat", sans-serif; font-weight: 800;
    font-size: 38px; letter-spacing: 1px; white-space: nowrap;
  }
  .brand-role {
    position: relative; margin-top: 6px; font-weight: 800; font-size: 20px;
    letter-spacing: 3px; color: var(--green); white-space: nowrap;
  }
  .headline {
    position: absolute; left: 48px; top: 460px;
    font-family: "Archivo Black", sans-serif; font-size: 86px; line-height: 1.02;
    text-transform: uppercase; text-shadow: 0 4px 10px rgba(0,0,0,.6);
  }
  .subhead {
    position: absolute; left: 48px; top: 672px;
    font-family: "Archivo Black", sans-serif; font-size: 56px; line-height: 1.1;
    text-transform: uppercase; text-shadow: 0 4px 10px rgba(0,0,0,.6);
  }
  .benefits {
    position: absolute; left: 48px; top: 808px;
    font-weight: 900; font-style: italic; font-size: 40px; line-height: 1.12; color: var(--green);
    text-shadow: 0 3px 8px rgba(0,0,0,.7);
  }
  .contact-bar {
    position: absolute; left: 24px; top: 972px; width: 560px; height: 68px;
    background: var(--panel); border: 3px solid var(--green-dark); border-left: none;
    display: flex; align-items: center; padding-left: 58px;
    font-weight: 900; font-style: italic; font-size: 34px; letter-spacing: 1px;
  }
  .contact-list {
    position: absolute; left: 0; top: 1052px; width: 640px; height: 148px;
    background: rgba(13,15,13,.9); padding: 10px 0 0 36px; list-style: none;
  }
  .contact-item {
    display: flex; align-items: center; gap: 14px; height: 44px;
    font-weight: 700; font-size: 28px; letter-spacing: .5px; white-space: nowrap;
  }
  .contact-icon { width: 28px; height: 28px; flex: none; }
</style>
</head>
<body>
<main class="post">
  <div class="gym-photo" role="img" aria-label="Mulher atlética de cabelo loiro em roupa de treino, equilibrando-se numa perna e alongando a outra acima da cabeça, dentro de uma academia"></div>
  <div class="shade"></div>

  <svg class="accents" width="1200" height="1200" viewBox="0 0 1200 1200" aria-hidden="true">
    <g fill="var(--green)">
      <rect x="600" y="10" width="90" height="14"/><rect x="720" y="10" width="90" height="14"/>
      <rect x="840" y="10" width="90" height="14"/><rect x="960" y="10" width="90" height="14"/>
      <rect x="1080" y="10" width="90" height="14"/>
      <rect x="660" y="1176" width="90" height="14"/><rect x="780" y="1176" width="90" height="14"/>
      <rect x="900" y="1176" width="90" height="14"/><rect x="1020" y="1176" width="90" height="14"/>
      <rect x="1140" y="1176" width="60" height="14"/>
    </g>
    <g stroke="var(--green)" stroke-width="3" fill="none" opacity=".8">
      <line x1="360" y1="1200" x2="1200" y2="360"/>
      <line x1="0" y1="760" x2="460" y2="300"/>
    </g>
    <polygon points="0,300 0,470 170,300" fill="var(--grey)" opacity=".8"/>
  </svg>

  <header class="brand">
    <svg class="brand-frame" width="564" height="228" viewBox="0 0 564 228" aria-hidden="true">
      <polyline points="4,224 4,4 470,4" fill="none" stroke="var(--green)" stroke-width="6"/>
      <polygon points="564,120 564,228 456,228" fill="var(--green)"/>
    </svg>
    <div class="brand-mark"></div>
    <div class="brand-name">RAFAEL DUARTE</div>
    <div class="brand-role">PERSONAL TRAINER</div>
  </header>

  <h1 class="headline">Qual o seu<br>objetivo?</h1>
  <p class="subhead">Posso te ajudar a<br>conquistá-lo!</p>
  <p class="benefits">Saúde, bem-estar, longevidade<br>e qualidade de vida!</p>

  <div class="contact-bar">ENTRE EM CONTATO</div>
  <ul class="contact-list">
    <li class="contact-item">
      <svg class="contact-icon" viewBox="0 0 24 24" aria-hidden="true"><circle cx="12" cy="12" r="10.5" fill="none" stroke="#fff" stroke-width="2"/><path d="M8.5 7.2l1.6-.4 1.2 2.6-1.1 1a7 7 0 0 0 3.4 3.4l1-1.1 2.6 1.2-.4 1.6c-4.2.6-8.9-4.1-8.3-8.3z" fill="#fff"/></svg>
      <span>11 98765-4321</span>
    </li>
    <li class="contact-item">
      <svg class="contact-icon" viewBox="0 0 24 24" aria-hidden="true"><circle cx="12" cy="12" r="10.5" fill="none" stroke="#fff" stroke-width="2"/></svg>
      <span>@personal_rafaelduarte</span>
    </li>
    <li class="contact-item">
      <svg class="contact-icon" viewBox="0 0 24 24" aria-hidden="true"><rect x="2" y="5" width="20" height="14" rx="2" fill="none" stroke="#fff" stroke-width="2"/><polyline points="3,6 12,13 21,6" fill="none" stroke="#fff" stroke-width="2"/></svg>
      <span>personal.rafael@mailbox.com</span>
    </li>
  </ul>
</main>
</body>
</html>
```